Psychic / Tarot Reader needs updated Friendbook Page

We need a new design for our Friendbook page.
Logo is attached and copy of new website that is being launched.
We need something fresh, simple and eye catching

current Friendbook: MoonWillowGlow

layout for entire Friendbook please

Target Market(s)

18 +

Requirements
Must have
• colours
• easy to use
• services

```html
<!DOCTYPE html>
<html lang="en">
<head>
<meta charset="utf-8">
<title>Moon Willow Glow – Page</title>
<link rel="stylesheet" href="https://fonts.googleapis.com/css2?family=Arimo:wght@400;700&family=Cinzel:wght@400;500&family=Cormorant+Garamond:wght@500;600&family=Josefin+Sans:wght@300;400&display=swap">
<style>
  :root{
    --bar-blue:#4267b2;
    --bar-dark:#29487d;
    --page-bg:#e9ebee;
    --card:#ffffff;
    --line:#dddfe2;
    --text:#1d2129;
    --muted:#606770;
    --link:#365899;
    --cta:#4267b2;
    --green:#42b72a;
    --violet:#8a2be2;
    --violet-deep:#5a1aa8;
    --title-lilac:#e6c6ff;
  }
  *{box-sizing:border-box;margin:0;padding:0}
  html,body{width:1200px;height:682px;overflow:hidden;background:var(--page-bg)}
  body{font-family:"Arimo",Arial,sans-serif;color:var(--text)}
  .stage{position:relative;width:1122px;height:638px;transform:scale(1.0695);transform-origin:0 0;overflow:hidden;background:var(--page-bg)}
  .abs{position:absolute}

  /* top bar */
  .topbar{left:0;top:0;width:1122px;height:45px;background:var(--bar-blue);border-top:2px solid var(--bar-dark)}
  .brand-mark{left:53px;top:10px;width:24px;height:24px;background:#fff;border-radius:2px}
  .search{left:85px;top:10px;width:445px;height:24px;background:#fff;border-radius:2px;font-size:14px;line-height:24px;padding-left:6px}
  .search-btn{right:0;top:0;width:45px;height:24px;background:#f6f7f9;border-left:1px solid var(--line);display:flex;align-items:center;justify-content:center}
  .user{left:722px;top:10px;display:flex;align-items:center;gap:8px;color:#fff;font-weight:700;font-size:12px}
  .avatar{width:22px;height:22px;background:#6b6b6b;border:1px solid #fff}
  .home{left:807px;top:16px;color:#fff;font-weight:700;font-size:12px;display:flex;gap:5px;align-items:center}
  .badge{background:var(--bar-dark);padding:1px 4px;border-radius:2px;font-size:11px}
  .top-icon{top:13px}
  .divider-v{left:1001px;top:12px;width:1px;height:22px;background:var(--bar-dark)}

  /* left column */
  .profile-pic{left:52px;top:59px;width:180px;height:180px;background:#fff;border:1px solid #ccc;padding:4px}
  .profile-inner{width:100%;height:100%;border:4px solid var(--violet-deep);display:flex;align-items:center;justify-content:center;text-align:center;padding:6px;overflow:hidden}
  .profile-name{font-family:"Josefin Sans",sans-serif;color:var(--violet);font-size:26px;line-height:1.1}
  .page-title{left:52px;top:252px;width:186px;font-size:21px;font-weight:400;white-space:nowrap}
  .page-handle{left:52px;top:283px;font-size:14px;color:var(--muted)}
  .nav{left:52px;top:318px;width:180px;list-style:none}
  .nav li{height:32px;line-height:32px;padding-left:11px;font-size:14px;color:var(--muted)}
  .nav .current{background:#dcdee3;border-left:3px solid var(--cta);padding-left:8px;color:var(--text);font-weight:700}
  .create{left:60px;top:527px;width:99px;height:22px;background:var(--green);color:#fff;font-weight:700;font-size:12px;line-height:22px;text-align:center;border-radius:2px}

  /* cover */
  .cover{left:244px;top:45px;width:820px;height:313px;background:radial-gradient(ellipse at 60% 40%,#b44cf0 0%,#8a2be2 45%,#5a12b8 100%);overflow:hidden;z-index:1}
  .cover-title{position:absolute;left:0;right:0;top:24px;text-align:center;font-family:"Cinzel",serif;font-size:38px;color:var(--title-lilac);letter-spacing:0.5px;white-space:nowrap}
  .services{position:absolute;left:0;right:0;top:92px;text-align:center;list-style:none;font-family:"Josefin Sans",sans-serif;color:#fff;font-size:21px;line-height:32px}
  .consult{position:absolute;left:116px;top:263px;width:600px;height:32px;background:rgba(70,10,130,.55);display:flex;align-items:center;justify-content:center;gap:14px;color:#fff;font-family:"Cormorant Garamond",serif;font-weight:600;font-size:15px;white-space:nowrap}
  .consult span{display:flex;align-items:center;gap:6px}

  /* action bar */
  .actions{left:244px;top:358px;width:820px;height:52px;background:var(--card);border:1px solid var(--line);border-top:none}
  .btn-group{position:absolute;left:12px;top:12px;display:flex}
  .btn{height:27px;border:1px solid #ccd0d5;background:#f6f7f9;font-size:12px;font-weight:700;color:#4b4f56;display:flex;align-items:center;gap:5px;padding:0 10px;margin-left:-1px}
  .call{position:absolute;left:520px;top:12px;width:182px;height:27px;background:var(--cta);color:#fff;font-size:14px;text-align:center;line-height:27px;border-radius:2px}
  .message{position:absolute;left:714px;top:12px;width:94px;height:27px}

  /* featured */
  .featured{left:244px;top:423px;width:500px;height:230px;background:var(--card);border:1px solid var(--line);overflow:hidden}
  .featured h2{position:absolute;left:12px;top:12px;font-size:14px;font-weight:700}
  .feature-card{position:absolute;top:40px;width:286px;height:200px;border:1px solid var(--line);background:#fff}
  .feature-head{height:40px;line-height:40px;padding-left:12px;font-size:14px;white-space:nowrap}
  .feature-head b{color:var(--link)}
  .feature-art{position:absolute;left:0;top:40px;width:100%;height:160px}
  .close-box{position:absolute;right:10px;top:12px;width:16px;height:16px;background:#bec2c9;color:#fff;font-size:13px;line-height:16px;text-align:center}
  .pager{left:719px;top:557px;width:26px;height:28px;background:#fff;border:1px solid var(--line);display:flex;align-items:center;justify-content:center}

  /* right column */
  .side{left:756px;width:308px;background:var(--card);border:1px solid var(--line);font-size:14px}
  .side-region{top:423px;height:42px;padding:14px 11px}
  .side-invite{top:478px;height:49px;padding:17px 11px;display:flex;align-items:center;gap:16px;font-size:12px;color:var(--text)}
  .side-about{top:540px;height:120px;padding:9px 11px}
  .side-about p{font-size:13px;line-height:16px}
  .rule{height:1px;background:var(--line);margin:10px 0 10px}
  .stats{display:flex;gap:20px;font-size:12px;line-height:16px}
  .stats span{width:240px}
</style>
</head>
<body>
<div class="stage">

  <header class="abs topbar">
    <div class="abs brand-mark" aria-hidden="true"></div>
    <div class="abs search">Moon Willow Glow
      <div class="abs search-btn">
        <svg width="14" height="14" viewBox="0 0 14 14"><circle cx="6" cy="6" r="4.5" fill="none" stroke="#4b4f56" stroke-width="1.8"/><line x1="9.3" y1="9.3" x2="13" y2="13" stroke="#4b4f56" stroke-width="2"/></svg>
      </div>
    </div>
    <div class="abs user"><div class="avatar"></div>Maya</div>
    <div class="abs home">Home <span class="badge">20+</span></div>
    <svg class="abs top-icon" style="left:898px" width="24" height="20" viewBox="0 0 24 20"><circle cx="15" cy="6" r="4" fill="#1d2a5a"/><path d="M8 19c0-5 3-7 7-7s7 2 7 7z" fill="#1d2a5a"/><circle cx="8" cy="7" r="3.5" fill="#1d2a5a"/><path d="M1 19c0-4 3-6 7-6 2 0 3 .5 3 .5S8 15 8 19z" fill="#1d2a5a"/></svg>
    <svg class="abs top-icon" style="left:935px" width="20" height="20" viewBox="0 0 20 20"><circle cx="10" cy="10" r="9" fill="#1d2a5a"/></svg>
    <svg class="abs top-icon" style="left:968px" width="20" height="20" viewBox="0 0 20 20"><circle cx="10" cy="10" r="9" fill="#1d2a5a"/><path d="M5 6c3 0 3 3 5 3s1 4 3 4M12 3c0 3 3 3 5 3" stroke="#4267b2" stroke-width="1.6" fill="none"/></svg>
    <div class="abs divider-v"></div>
    <svg class="abs top-icon" style="left:1023px" width="20" height="20" viewBox="0 0 20 20"><circle cx="10" cy="10" r="9" fill="#1d2a5a"/><text x="10" y="15" text-anchor="middle" font-family="Arimo, sans-serif" font-weight="700" font-size="13" fill="#4267b2">?</text></svg>
    <svg class="abs" style="left:1054px;top:19px" width="11" height="7" viewBox="0 0 11 7"><path d="M0 0h11L5.5 7z" fill="#1d2a5a"/></svg>
  </header>

  <aside>
    <div class="abs profile-pic">
      <div class="profile-inner"><span class="profile-name">MoonWillow<wbr>Glow</span></div>
    </div>
    <h1 class="abs page-title">Moon Willow Glow</h1>
    <div class="abs page-handle">@moonwillowglow</div>
    <ul class="abs nav">
      <li class="current">Home</li>
      <li>About</li>
      <li>Services</li>
      <li>Photos</li>
      <li>Likes</li>
      <li>Posts</li>
    </ul>
    <div class="abs create">Create a Page</div>
  </aside>

  <section class="abs cover">
    <div class="cover-title">WELCOME TO MOON WILLOW GLOW</div>
    <ul class="services">
      <li>Tarot Card Reader</li>
      <li>Dream Interpretation</li>
      <li>Reiki Healer</li>
      <li>Realm Reader</li>
    </ul>
    <div class="consult">
      <span>FOR CONSULTATION :</span>
      <span><svg width="12" height="13" viewBox="0 0 12 13"><path d="M2 1l3 0 1 3-2 1.5c1 2 2 3 3.5 3.5L9 7l3 1v3c-6 1-11-4-10-10z" fill="#fff"/></svg>+61 400 555 017</span>
      <span><svg width="15" height="11" viewBox="0 0 15 11"><rect x="0.8" y="0.8" width="13.4" height="9.4" fill="none" stroke="#fff" stroke-width="1.4"/><path d="M1 1l6.5 5L14 1" fill="none" stroke="#fff" stroke-width="1.4"/></svg>luna@moonwillowglow.com.au</span>
    </div>
  </section>

  <div class="abs actions">
    <div class="btn-group">
      <div class="btn"><svg width="12" height="12" viewBox="0 0 12 12"><path d="M0 5h3v7H0zM4 5l3-5c1 0 2 1 1.5 2.5L8 4h3.5c.5 0 1 .5.5 1.5l-1.5 6H4z" fill="#90949c"/></svg>Like</div>
      <div class="btn"><svg width="12" height="12" viewBox="0 0 12 12"><circle cx="2" cy="10" r="1.6" fill="#90949c"/><path d="M1 5a6 6 0 016 6M1 1a10 10 0 0110 10" fill="none" stroke="#90949c" stroke-width="1.6"/></svg>Follow</div>
      <div class="btn"><svg width="13" height="11" viewBox="0 0 13 11"><path d="M7 0l6 5-6 5V7C3 7 1 8 0 11 0 6 3 3 7 3z" fill="#90949c"/></svg>Share</div>
      <div class="btn" style="width:34px;justify-content:center;color:#90949c">···</div>
    </div>
    <div class="call">Call Now</div>
    <div class="btn message"><svg width="13" height="13" viewBox="0 0 13 13"><circle cx="6.5" cy="6" r="5.5" fill="#90949c"/></svg>Message</div>
  </div>

  <section class="abs featured">
    <h2>Featured for you</h2>
    <div class="feature-card" style="left:7px">
      <div class="feature-head">Get in touch with <b>Moon Willow Glow</b></div>
      <div class="close-box">×</div>
      <div class="feature-art" role="img" aria-label="Fantasy artwork of a figure in white beside a large pale lion" style="background:linear-gradient(135deg,#4a56a8 0%,#c9ccd8 50%,#8b8fa6 100%)"></div>
    </div>
    <div class="feature-card" style="left:300px">
      <div class="feature-head">Save <b>Moon Willow Glow</b> to visit it later</div>
      <div class="feature-art" role="img" aria-label="Quote graphic about living positively" style="background:#f1eff4"></div>
    </div>
  </section>
  <div class="abs pager"><svg width="8" height="12" viewBox="0 0 8 12"><path d="M1 1l5 5-5 5" fill="none" stroke="#1d2129" stroke-width="2"/></svg></div>

  <div class="abs side side-region">Region in Coralbay, Queensland</div>
  <div class="abs side side-invite">
    <svg width="20" height="18" viewBox="0 0 20 18"><circle cx="7" cy="5" r="4" fill="#bec2c9"/><path d="M0 17c0-5 3-7 7-7s7 2 7 7z" fill="#bec2c9"/><path d="M16 3v6M13 6h6" stroke="#bec2c9" stroke-width="2"/></svg>
    Invite friends to like this Page
  </div>
  <div class="abs side side-about">
    <p>Tarot Card Reader, Dream Interpretation, Reiki Healer, Realm Reader</p>
    <div class="rule"></div>
    <div class="stats">
      <svg width="14" height="14" viewBox="0 0 12 12"><path d="M0 5h3v7H0zM4 5l3-5c1 0 2 1 1.5 2.5L8 4h3.5c.5 0 1 .5.5 1.5l-1.5 6H4z" fill="#606770"/></svg>
      <span>504 people like this and 491 people follow this</span>
    </div>
  </div>

</div>
</body>
</html>
```